Craft beer central! New brew pub needs website that doesn't suck.

We are a new brewpub in Picton, Ontario. We have a kitchen and are about to start with our own beer. Currently I have a really horrid horrid website.

Check it out www.thehollowlarder.example (please don't laugh too hard)

I'm on Facebook as well which might give a better idea of who we are
(it's my main social media)
https://www.facebook.com/millstreamslarder

(there is a long story with the name difference)

I want something that I can edit myself (things like events, dates,etc), change the menu pdf, add events, have a contact page, have a gallery of pics, our beer/wine menu and eventually what we are putting on tap ourselves.

We currently have 16 craft beers on tap, local wine and our tag line is "explore the bounty of the county".
Updates

Project Deadline Extended
Reason: Sorry to have extended it. Have a few things on this week. Cheers,

Target Market(s)

craft beer, tourists.

Industry/Entity Type

Hospitality

Number of Pages Required

4 page

Font styles to use
Other font styles liked:
• Museo slab and next bold.

Requirements
Must have
• Must be able to attach a menu pdf (I have a food menu and beer/wine menu)
• Must have an events page so I can edit/ add them as we go on
• contacts page
• Must have a gallery that I can edit/swap pictures.
Nice to have
• Modern, hip looking page. Love black, white, grey and a splash of red.
Should not have
• be a feminine looking site. look at our Facebook page to look at our decor.

```html
<!DOCTYPE html>
<html lang="en">
<head>
<meta charset="utf-8">
<title>The Hollow Larder</title>
<link href="https://fonts.googleapis.com/css2?family=Arvo:wght@400;700&family=Courier+Prime:wght@400;700&display=swap" rel="stylesheet">
<style>
:root{
  --paper:#e8e7e3;
  --paper-light:#f2f1ed;
  --ink:#1b1b1b;
  --ink-soft:#3a3a3a;
  --photo-dark:#2a2724;
  --photo-mid:#6b645c;
  --cream:#efe6d2;
  --red:#d42a22;
  --white:#ffffff;
}
*{margin:0;padding:0;box-sizing:border-box}
html,body{width:1200px;height:2168px;overflow:hidden}
body{background:var(--paper);color:var(--ink);font-family:"Courier Prime",monospace;position:relative}

.hero{position:absolute;left:0;top:0;width:1200px;height:780px;
  background:radial-gradient(ellipse at 50% 35%,var(--photo-mid) 0%,#4a4540 40%,var(--photo-dark) 85%)}
.top-bar{position:absolute;left:0;top:0;width:1200px;height:80px;display:flex;justify-content:space-between;align-items:center;padding:0 40px}
.top-item{display:flex;align-items:center;gap:12px;background:var(--paper-light);padding:8px 18px;font-size:26px;color:var(--ink)}
.brand{position:absolute;left:0;top:250px;width:1200px;text-align:center;font-family:"Arvo",serif;font-weight:700;color:var(--white);font-size:80px;letter-spacing:2px;line-height:96px;white-space:nowrap}
.brand-sub{position:absolute;left:0;top:368px;width:1200px;text-align:center;font-family:"Arvo",serif;font-weight:700;color:var(--white);font-size:32px;line-height:40px}

.nav-icons{position:absolute;left:140px;top:560px;width:940px;display:flex;justify-content:space-between}
.nav-icon{width:172px;height:172px;border-radius:50%;background:var(--cream);display:flex;align-items:center;justify-content:center}
.nav-strip{position:absolute;left:0;top:740px;width:1200px;height:90px;background:var(--paper)}
.nav{position:absolute;left:140px;top:752px;width:940px;display:flex;justify-content:space-between;list-style:none}
.nav li{width:172px;text-align:center;font-size:34px;color:var(--ink-soft);white-space:nowrap}
.nav li.active span{background:var(--ink);color:var(--white);padding:0 22px}

.intro{position:absolute;left:0;top:835px;width:1200px;text-align:center}
.intro h1{font-family:"Arvo",serif;font-weight:400;font-size:48px}
.intro p{width:930px;margin:24px auto 0;font-size:19px;line-height:25px}
.dots{position:absolute;left:0;top:1040px;width:1200px;display:flex;justify-content:center;gap:56px}
.dot{width:52px;height:52px;border-radius:50%;background:var(--white);display:flex;align-items:center;justify-content:center}

.news{position:absolute;left:88px;top:1165px;width:1030px}
.poster{position:absolute;left:0;top:0;width:230px;height:360px;background:linear-gradient(#e6e0cf,#cfc6b0);box-shadow:2px 3px 6px rgba(0,0,0,.3)}
.news-body{position:absolute;left:302px;top:0;width:760px}
.label{display:inline-block;background:var(--ink);color:var(--white);font-family:"Arvo",serif;font-size:32px;padding:2px 16px}
.news-body h2{font-family:"Arvo",serif;font-weight:400;font-size:42px;margin-top:14px}
.news-body p{font-size:19px;line-height:25px;margin-top:18px}
.more{font-size:24px;margin-top:28px;display:block}

.gallery{position:absolute;left:150px;top:1640px;width:900px;height:320px}
.polaroid{position:absolute;width:225px;height:270px;background:var(--white);padding:14px 14px 56px;box-shadow:2px 4px 8px rgba(0,0,0,.35)}
.polaroid div{width:100%;height:100%}

.footer{position:absolute;left:0;top:2030px;width:1200px;height:138px;background:var(--ink);color:var(--white);display:flex;align-items:center;padding:0 56px}
.footer-brand{font-family:"Arvo",serif;font-weight:700;font-size:22px;width:260px;line-height:1;white-space:nowrap}
.footer-address{font-size:22px;line-height:30px;margin-left:30px}
.follow{margin-left:auto;display:flex;align-items:center;gap:16px;font-size:24px}
.follow span.sq{width:30px;height:30px;background:var(--white);display:inline-block}
</style>
</head>
<body>
<header class="hero" role="img" aria-label="Interior photograph of the brew pub bar in warm grey tones"></header>
<div class="top-bar">
  <div class="top-item">
    <svg width="20" height="28" viewBox="0 0 20 28"><path d="M10 0C4.5 0 0 4.4 0 9.8 0 17 10 28 10 28s10-11 10-18.2C20 4.4 15.5 0 10 0z" fill="#1b1b1b"/><circle cx="10" cy="10" r="4" fill="#f2f1ed"/></svg>
    148 Mill Street West
  </div>
  <div class="top-item">
    <svg width="30" height="24" viewBox="0 0 30 24"><path d="M2 8c0-4 6-6 13-6s13 2 13 6v3h-7V8H9v3H2z" fill="#1b1b1b"/><rect x="6" y="12" width="18" height="11" rx="2" fill="#1b1b1b"/></svg>
    613-555-0142
  </div>
</div>
<div class="brand">THE HOLLOW LARDER</div>
<div class="brand-sub">Millstream County</div>

<div class="nav-strip"></div>
<div class="nav-icons">
  <div class="nav-icon"><svg width="100" height="90" viewBox="0 0 100 90"><path d="M50 4 4 44h12v42h26V60h16v26h26V44h12z" fill="#1b1b1b"/></svg></div>
  <div class="nav-icon"><svg width="100" height="100" viewBox="0 0 100 100"><path d="M24 8h10v22c6 4 8 10 8 16v50H16V46c0-6 2-12 8-16z" fill="#1b1b1b"/><path d="M56 36h30l-4 60H60z" fill="#1b1b1b"/></svg></div>
  <div class="nav-icon"><svg width="90" height="100" viewBox="0 0 90 100"><path d="M20 6v30M14 6v24c0 6 3 10 6 10s6-4 6-10V6M20 40v56" stroke="#1b1b1b" stroke-width="6" fill="none" stroke-linecap="round"/><path d="M64 6c-10 8-12 28-4 38v52h8V6z" fill="#1b1b1b"/></svg></div>
  <div class="nav-icon"><svg width="110" height="90" viewBox="0 0 110 90"><path d="M6 28C6 12 30 6 55 6s49 6 49 22v10H80V26H30v12H6z" fill="#1b1b1b"/><path d="M26 40h58l8 44H18z" fill="#1b1b1b"/><circle cx="55" cy="62" r="12" fill="#efe6d2"/></svg></div>
</div>
<ul class="nav">
  <li class="active"><span>home</span></li>
  <li>our beer</li>
  <li>menu</li>
  <li>contact</li>
</ul>

<section class="intro">
  <h1>Explore the bounty of the county...</h1>
  <p>Lorem ipsum dolor sit amet, consectetur adipiscing elit, sed do eiusmod tempor incididunt ut labore et dolore magna aliqua. Ut enim ad minim veniam, quis nostrud exercitation ullamco laboris nisi ut aliquip ex ea commodo consequat.</p>
</section>
<div class="dots">
  <div class="dot"><svg width="30" height="30" viewBox="0 0 30 30"><g stroke="#d42a22" stroke-width="7" stroke-linecap="round"><path d="M15 3v24M4.6 9l20.8 12M4.6 21l20.8-12"/></g></svg></div>
  <div class="dot"><svg width="30" height="30" viewBox="0 0 30 30"><g stroke="#d42a22" stroke-width="7" stroke-linecap="round"><path d="M15 3v24M4.6 9l20.8 12M4.6 21l20.8-12"/></g></svg></div>
  <div class="dot"><svg width="30" height="30" viewBox="0 0 30 30"><g stroke="#d42a22" stroke-width="7" stroke-linecap="round"><path d="M15 3v24M4.6 9l20.8 12M4.6 21l20.8-12"/></g></svg></div>
  <div class="dot"><svg width="30" height="30" viewBox="0 0 30 30"><g stroke="#d42a22" stroke-width="7" stroke-linecap="round"><path d="M15 3v24M4.6 9l20.8 12M4.6 21l20.8-12"/></g></svg></div>
</div>

<section class="news">
  <div class="poster" role="img" aria-label="Event poster for the Stonecrop sampling night"></div>
  <div class="news-body">
    <span class="label">Latest News</span>
    <h2>Stonecrop sampling event</h2>
    <p>Join us on Wednesday, July 29th at 6:30 pm for a special Stonecrop Sampling event!</p>
    <p>Lorem ipsum dolor sit amet, consectetur adipiscing elit, sed do eiusmod tempor incididunt ut labore et dolore magna aliqua. Ut enim ad minim veniam, quis nostrud exercitation ullamco laboris nisi ut aliquip ex ea commodo consequat.</p>
    <span class="more">more</span>
  </div>
</section>

<section class="gallery">
  <div class="polaroid" style="left:0;top:20px;transform:rotate(-5deg)"><div role="img" aria-label="Photo of the pub patio" style="background:linear-gradient(#8fa7b8,#a0764c)"></div></div>
  <div class="polaroid" style="left:215px;top:0;transform:rotate(3deg)"><div role="img" aria-label="Photo of local wine bottles" style="background:linear-gradient(#b8ad98,#5c5a44)"></div></div>
  <div class="polaroid" style="left:440px;top:15px;transform:rotate(-2deg)"><div role="img" aria-label="Photo of a cocktail" style="background:linear-gradient(#c9b89b,#8a6a3c)"></div></div>
  <div class="polaroid" style="left:665px;top:5px;transform:rotate(6deg)"><div role="img" aria-label="Photo of the dining room" style="background:linear-gradient(#b68a5a,#4a3424)"></div></div>
</section>

<footer class="footer">
  <div class="footer-brand">THE HOLLOW LARDER</div>
  <div class="footer-address">148 Mill Street | Millbrook | Ontario K0A1B0<br>613-555-0142</div>
  <div class="follow">follow us: <span class="sq"></span><span class="sq"></span></div>
</footer>
</body>
</html>
```